Eastlane Holdings Card

I would like a modern, eye catching card based off my logo design.
Info to include:
Tomas Velden (Card Name)
eastlaneholdings.com (Website)
555 283 6091 (Office/fax)
555 736 2840 (Business Cell)
tomas@eastlaneholdings.com (Work email)

Target Market(s)

Commercial real estate brokers, property owners.

Colors
ec1f27
757575

Requirements
Must have
• Name and info above. Not be lame!:)

```html
<!DOCTYPE html>
<html lang="en">
<head>
<meta charset="utf-8">
<title>Eastlane Holdings – Business Card</title>
<link rel="stylesheet" href="https://fonts.googleapis.com/css2?family=Montserrat:wght@600;700&family=Arimo:wght@400;700&display=swap">
<style>
  :root {
    --brand-red: #9b0a10;
    --brand-red-bright: #ec1f27;
    --brand-grey: #757575;
    --dark-grey: #4a4a4a;
    --ink: #1d1d1d;
    --paper: #f7f7f7;
    --backdrop: #2b2b2b;
  }
  * { box-sizing: border-box; margin: 0; padding: 0; }
  html, body { width: 1200px; height: 997px; overflow: hidden; }
  body {
    background: var(--backdrop);
    font-family: "Arimo", Arial, sans-serif;
    position: relative;
  }
  .card {
    position: absolute;
    width: 540px;
    height: 309px;
    border-radius: 3px;
    box-shadow: 0 14px 30px rgba(0,0,0,.45);
    overflow: hidden;
  }

  /* Front */
  .card-front {
    left: 60px; top: 150px;
    background: var(--brand-red);
    color: #fff;
    display: flex; flex-direction: column; align-items: center; justify-content: center;
  }
  .front-mark {
    display: flex; align-items: center; gap: 14px;
    margin-bottom: 10px;
  }
  .front-mark .mark-square { width: 40px; height: 40px; background: #fff; }
  .brand-name {
    font-family: "Montserrat", sans-serif; font-weight: 700;
    text-transform: uppercase; letter-spacing: 1px;
  }
  .card-front .brand-name { font-size: 30px; color: #fff; }
  .tagline {
    display: flex; align-items: center; gap: 10px;
    font-family: "Montserrat", sans-serif; font-weight: 600;
    text-transform: uppercase; letter-spacing: 3px;
  }
  .tagline::before, .tagline::after { content: ""; height: 2px; background: currentColor; }
  .card-front .tagline { font-size: 12px; }
  .card-front .tagline::before, .card-front .tagline::after { width: 60px; }
  .website {
    margin-top: 26px;
    font-family: "Montserrat", sans-serif; font-weight: 600;
    font-size: 14px; letter-spacing: 3px;
  }

  /* Back */
  .card-back {
    left: 600px; top: 520px;
    background: var(--paper);
    color: var(--ink);
  }
  .side-strip {
    position: absolute; left: 0; top: 0; bottom: 0; width: 26px;
    background: var(--brand-red);
  }
  .side-strip .strip-block {
    position: absolute; left: 0; top: 112px; width: 26px; height: 30px;
    background: var(--dark-grey);
  }
  .back-header { position: absolute; left: 48px; top: 30px; color: var(--brand-red); }
  .back-header .brand-name { font-size: 15px; }
  .back-header .tagline { font-size: 7px; letter-spacing: 2px; color: var(--dark-grey); }
  .back-header .tagline::before { width: 18px; background: var(--brand-red); }
  .back-header .tagline::after { width: 18px; background: var(--brand-red); }
  .person { position: absolute; left: 48px; top: 108px; }
  .person-name { font-weight: 700; font-size: 19px; color: var(--brand-red); }
  .person-title { font-size: 13px; margin-top: 2px; }
  .contact-list {
    position: absolute; left: 48px; bottom: 26px;
    list-style: none; font-size: 15px;
  }
  .contact-list li { display: flex; align-items: center; gap: 12px; height: 25px; }
  .contact-list svg { width: 12px; height: 12px; fill: var(--brand-red); flex: none; }
  .back-mark {
    position: absolute; right: 34px; top: 48px;
    width: 160px; height: 160px;
    border: 14px solid var(--dark-grey);
    display: flex; align-items: center; justify-content: center;
  }
  .back-mark .mark-square { width: 60px; height: 60px; background: var(--brand-red); }
  .back-mark-label {
    position: absolute; right: 34px; top: 222px; width: 160px; text-align: center;
    font-family: "Montserrat", sans-serif; font-weight: 700; font-size: 14px;
    text-transform: uppercase; letter-spacing: 1px; color: var(--dark-grey);
  }
</style>
</head>
<body>

<section class="card card-front" aria-label="Card front">
  <div class="front-mark">
    <span class="mark-square" aria-hidden="true"></span>
    <span class="brand-name">Eastlane Holdings</span>
  </div>
  <div class="tagline">Construction &amp; Roofing</div>
  <div class="website">www.eastlaneholdings.com</div>
</section>

<section class="card card-back" aria-label="Card back">
  <div class="side-strip"><span class="strip-block"></span></div>

  <header class="back-header">
    <div class="brand-name">Eastlane Holdings</div>
    <div class="tagline">Construction &amp; Roofing</div>
  </header>

  <div class="person">
    <div class="person-name">Tomas Velden</div>
    <div class="person-title">Director of Sales &amp; Marketing</div>
  </div>

  <ul class="contact-list">
    <li>
      <svg viewBox="0 0 12 12" aria-hidden="true"><path d="M1 4c0-2 2-3 5-3s5 1 5 3l-2 1-1-2H4L3 5zM3 6h6l1 5H2z"/></svg>
      555 283 6091
    </li>
    <li>
      <svg viewBox="0 0 12 12" aria-hidden="true"><path d="M3 0h6v12H3zM4 1.5v8h4v-8z"/></svg>
      555 736 2840
    </li>
    <li>
      <svg viewBox="0 0 12 12" aria-hidden="true"><path d="M0 2h12v8H0zM1 3v.5l5 3.5 5-3.5V3z"/></svg>
      tomas@eastlaneholdings.com
    </li>
  </ul>

  <div class="back-mark" aria-hidden="true"><span class="mark-square"></span></div>
  <div class="back-mark-label">Eastlane Holdings</div>
</section>

</body>
</html>
```